Business Card Design.

Life and Wellness Coach
www.brightpathwell.com
Want to use my name as the logo it could be the initials TRH or my full name. I want to trade mark me.
I like clean lines and simple designs, but it pops using the colors scheme (one or two colors) on the website.
I provide life and health coaching virtually and in person. My services include: Nutrition Response Testing, Allergy Elimination Testing, Wellness Coaching, Life Coaching. Life and Health Assessments, and I sell foundational health products and specialized nutrition. Use colors that represent healing and trust.
Target Market(s)
Women for the ages of 30 - 60
Industry/Entity Type
Health
Contact Information for Business Card
Tessa Ravenna Holloway
Life and Wellness Coach
tessa@coachtrh.com
www.brightpathwell.com
443-781-6392
Health is not an event it's a lifestyle (tag line or if you have a better tag line)

```html
<!DOCTYPE html>
<html lang="en">
<head>
<meta charset="utf-8">
<title>Tessa Ravenna Holloway — Business Card</title>
<link href="https://fonts.googleapis.com/css2?family=Fira+Sans:wght@400;600&display=swap" rel="stylesheet">
<style>
  :root {
    --page-bg: #e6e8ea;
    --card-bg: #ffffff;
    --accent: #b2466f;
    --rule: #4a4a4a;
    --portrait-top: #6a4a3c;
    --portrait-bottom: #2c3f8f;
  }
  * { margin: 0; padding: 0; box-sizing: border-box; }
  html, body {
    width: 1200px; height: 1000px; overflow: hidden;
    background: var(--page-bg);
    font-family: "Fira Sans", sans-serif;
  }
  .card {
    position: absolute;
    left: 100px; top: 214px;
    width: 1000px; height: 572px;
    background: var(--card-bg);
    box-shadow: 0 6px 24px rgba(0,0,0,0.18);
    overflow: hidden;
  }
  .portrait {
    position: absolute;
    left: 0; top: 170px;
    width: 440px; height: 402px;
    background: linear-gradient(180deg, var(--portrait-top) 0%, #b98e78 45%, #c9a48e 65%, var(--portrait-bottom) 100%);
  }
  .identity {
    position: absolute;
    right: 90px; top: 48px;
    text-align: right;
    color: var(--accent);
  }
  .identity .name { font-weight: 600; font-size: 34px; line-height: 1.15; }
  .identity .role { font-weight: 400; font-size: 24px; line-height: 1.3; }
  .contact {
    position: absolute;
    right: 70px; top: 280px;
    text-align: right;
    color: var(--accent);
    font-size: 26px;
    line-height: 1.35;
    list-style: none;
  }
  .divider {
    position: absolute;
    left: 440px; right: 0; top: 420px;
    height: 3px;
    background: var(--rule);
  }
  .tagline {
    position: absolute;
    right: 50px; top: 446px;
    color: var(--accent);
    font-size: 30px;
    font-weight: 400;
  }
</style>
</head>
<body>
  <main class="card">
    <div class="portrait" role="img" aria-label="Portrait photograph of the coach, smiling, in a blue top"></div>
    <header class="identity">
      <h1 class="name">Tessa Ravenna Holloway</h1>
      <p class="role">Life and Wellness Coach</p>
    </header>
    <ul class="contact">
      <li>Phone : 443-781-6392</li>
      <li>Email : tessa@coachtrh.com</li>
      <li>Website : www.brightpathwell.com</li>
    </ul>
    <div class="divider"></div>
    <p class="tagline">Health is not an event it's a lifestyle</p>
  </main>
</body>
</html>
```